Brightvale Outfitters Co. Shopify (Rebrand)

FULL WEBSITE AUDIT AND REBRAND
CLEAN Simplistic LOOK
Little Friction, Functional
COLORS: BLUE,ORANGE,BLACK, WHITE.
I upload a google doc with further information and social media sites to get a better understanding a design concept.
NEW WEBISTE LINK: www.brightvaleoutfitters.com

Front page photos

Consistent photography
Good product descriptions
How we started brand story 🎯
Brand ascetic🎯
Home page call to Action
***OUR BRIGHTVALE***
this will highlight brand story and customer photos and reviews
Great Clothing Brand Websites I take inspiration from for website

https://www.skyblnkr.com

https://harborlanternfund.org

https://quietsolenne.com

https://velvetorbitz.com/?ref=QX7bLmT2pRw9KcVn4HsYdE3uJfZaG8oB1tNeMiW6xCyAq5DkUgPv0lSjOhXrFb
Setup for easy accessibility of photography with new collections.

```html
<!DOCTYPE html>
<html lang="en">
<head>
<meta charset="utf-8">
<title>Brightvale Outfitters Co.</title>
<link href="https://fonts.googleapis.com/css2?family=Lato:wght@400;700;900&family=Orbitron:wght@600;700&display=swap" rel="stylesheet">
<style>
:root{
  --blue:#1d5c94;
  --blue-dark:#184e7e;
  --orange:#ef6420;
  --orange-deep:#d8571b;
  --ink:#1e1e1e;
  --text:#555;
  --blush:#fbf2ee;
  --mist:#eef4f9;
  --white:#fff;
}
*{box-sizing:border-box;margin:0;padding:0}
html,body{width:1200px;height:4515px;overflow:hidden}
body{position:relative;font-family:"Lato",sans-serif;color:var(--text);background:var(--white)}
.abs{position:absolute}
.brand-name{font-family:"Lato",sans-serif;font-weight:700;color:var(--blue);white-space:nowrap}
.dot{display:inline-block;border-radius:50%}

/* top bar */
.topbar{top:0;left:0;width:1200px;height:37px;background:var(--blue);color:#fff;font-size:13px}
.topbar .phone{left:110px;top:10px;display:flex;align-items:center;gap:6px}
.topbar .socials{left:307px;top:7px;display:flex;gap:5px}
.socials span{width:22px;height:22px;border-radius:50%;background:var(--orange)}
.topbar .account{right:110px;top:10px;font-weight:700;display:flex;gap:26px}

/* header */
.header{top:37px;left:0;width:1200px;height:108px;background:#fff;border-bottom:1px solid #eee}
.logo{display:flex;align-items:center;gap:12px}
.logo .dot{width:56px;height:56px;background:var(--blue)}
.header .logo{left:102px;top:26px}
.header .logo .brand-name{font-size:19px}
.nav{left:444px;top:47px;display:flex;gap:21px;font-size:13px;font-weight:700;color:#222}
.nav .active{color:var(--orange)}
.search{left:876px;top:36px;width:210px;height:40px;border:1px solid #ddd;border-radius:20px;box-shadow:0 2px 6px rgba(0,0,0,.06);display:flex;align-items:center;padding-left:20px;gap:8px;font-size:13px;color:#888}

/* hero */
.hero{top:145px;left:0;width:1200px;height:670px;overflow:hidden}
.hero-photo{position:absolute;inset:0;background:linear-gradient(135deg,#3c4a57 0%,#5d6b78 40%,#2f3a45 100%)}
.hero-title{top:262px;width:1200px;text-align:center;font-family:"Orbitron",sans-serif;font-weight:700;font-size:38px;line-height:47px;color:#fff;letter-spacing:1px}
.btn{display:inline-block;background:var(--orange);color:#fff;font-weight:700;font-size:14px;border-radius:24px;text-align:center}
.hero .btn{left:535px;top:383px;width:130px;height:46px;line-height:46px}
.hero-wave{left:0;top:0}
.dots{top:600px;left:563px;display:flex;gap:9px}
.dots span{width:12px;height:12px;border-radius:50%;border:2px solid #fff}
.dots .on{background:#fff}

/* section headings */
.mark{width:52px;height:52px;border-radius:50%;background:var(--blue);left:574px}
.heading{width:1200px;text-align:center;font-family:"Orbitron",sans-serif;font-weight:700;font-size:35px;color:var(--blue);letter-spacing:1px}

/* collections */
.collection{top:1051px;height:329px;border:6px solid #fff;box-shadow:0 4px 14px rgba(0,0,0,.18)}
.collection .label{position:absolute;inset:0;display:flex;align-items:center;justify-content:center;font-size:24px;font-weight:700;color:#fff}
.c-hoodies{left:112px;width:473px;background:linear-gradient(160deg,#d9b08a,#7c5d49 60%,#2a2320)}
.c-tees{left:615px;width:473px;background:linear-gradient(160deg,#3f7fb3,#7aa7c9 50%,#4a3528)}

/* featured */
.featured{top:1498px;left:0;width:1200px;height:692px;background:var(--blush)}
.product{top:231px;width:294px;height:385px;background:#fff;box-shadow:0 3px 12px rgba(0,0,0,.08);text-align:center}
.product.is-active{border:2px solid var(--orange)}
.product .shot{position:absolute;left:67px;top:35px;width:160px;height:180px;border-radius:8px}
.product .btn{position:absolute;left:82px;top:170px;width:130px;height:44px;line-height:44px}
.product h3{position:absolute;top:253px;width:100%;font-size:15px;font-weight:900;color:#222}
.product p{position:absolute;top:286px;left:30px;right:30px;font-size:14px;line-height:23px}
.product .price{position:absolute;top:340px;width:100%;font-size:16px;font-weight:900;color:var(--blue)}
.arrow{width:34px;height:34px;border-radius:50%;background:#fff;box-shadow:0 2px 8px rgba(0,0,0,.15);display:flex;align-items:center;justify-content:center}

/* mission */
.mission{top:2190px;left:0;width:1200px;height:620px;background:linear-gradient(120deg,#e0601f,var(--orange-deep) 60%,#c94f17)}
.mission .mark{background:#fff}
.mission .heading{color:#fff}
.mbox{top:222px;height:332px;border:3px solid #fff;color:#fff;text-align:center}
.mbox .icon{position:absolute;top:36px;width:90px;height:90px;border-radius:50%;background:#fff;display:flex;align-items:center;justify-content:center}
.mbox h3{position:absolute;top:155px;width:100%;font-size:19px;font-weight:700}
.mbox p{position:absolute;top:193px;left:30px;right:30px;font-size:14px;line-height:26px}

/* story */
.story-photo{left:112px;top:2940px;width:487px;height:362px;border:6px solid #fff;box-shadow:0 4px 14px rgba(0,0,0,.18);background:linear-gradient(170deg,#c9dbe4,#8fa9a2 45%,#b7b3ad)}
.story .mark{left:848px}
.story h2{left:674px;width:400px;text-align:center;font-family:"Orbitron",sans-serif;font-weight:700;font-size:28px;color:var(--blue)}
.story p{left:660px;width:428px;text-align:center;font-size:14px;line-height:25px}
.story .btn{left:804px;top:3218px;width:140px;height:46px;line-height:46px}

/* reviews */
.reviews{top:3429px;left:0;width:1200px;height:700px;background:var(--mist)}
.review{top:227px;width:308px;height:300px;background:#fff;border-radius:8px;box-shadow:0 3px 12px rgba(0,0,0,.06);text-align:center}
.review .avatar{position:absolute;left:114px;top:22px;width:80px;height:80px;border-radius:50%;border:4px solid #e5e9ee;background:linear-gradient(#b9c6d3,#6f7f8f)}
.review p{position:absolute;top:122px;left:20px;right:20px;font-size:16px;line-height:27px;color:#666;z-index:1}
.review .quote{position:absolute;font-family:Georgia,serif;font-size:90px;line-height:1;color:#ececec}
.review .who{position:absolute;top:236px;width:100%;font-size:17px;font-weight:700;color:var(--blue)}
.review .stars{position:absolute;top:262px;width:100%;font-size:12px;color:var(--orange);letter-spacing:1px}

/* footer */
.footer-arch{left:0;top:4040px}
.footer{top:4140px;left:0;width:1200px;height:375px;color:#fff}
.footer .logo{left:462px;top:12px}
.footer .logo .dot{background:#fff;width:64px;height:64px}
.footer .logo .brand-name{color:#fff;font-size:21px}
.footer h4{font-size:20px;font-weight:700;letter-spacing:.3px}
.links{font-size:14px;line-height:35px}
.newsletter-input{left:596px;top:155px;width:300px;height:42px;border-bottom:1px solid #888;font-size:13px;padding-top:12px}
.footer .btn{left:932px;top:147px;width:136px;height:50px;line-height:50px;font-size:16px}
.contact{font-size:14px;display:flex;align-items:center;gap:12px}
.footer .socials{left:334px;top:265px;display:flex;gap:3px}
.footer .socials span{width:24px;height:24px}
.rule{left:112px;top:312px;width:976px;height:1px;background:#444}
.copy{left:448px;top:331px;font-size:12px}
.cards{left:883px;top:324px;display:flex;gap:4px}
.cards span{width:37px;height:23px;background:#fff;border-radius:2px}
</style>
</head>
<body>

<div class="abs topbar">
  <div class="abs phone">
    <svg width="12" height="12" viewBox="0 0 24 24"><path fill="#fff" d="M6.6 10.8a15 15 0 0 0 6.6 6.6l2.2-2.2c.3-.3.7-.4 1-.2 1.1.4 2.3.6 3.6.6.6 0 1 .4 1 1V20c0 .6-.4 1-1 1A17 17 0 0 1 3 4c0-.6.4-1 1-1h3.5c.6 0 1 .4 1 1 0 1.3.2 2.5.6 3.6.1.3 0 .7-.2 1z"/></svg>
    +1555-014-2290
  </div>
  <div class="abs socials"><span></span><span></span><span></span><span></span><span></span></div>
  <div class="abs account"><span>My Account</span><span>Cart (0)</span></div>
</div>

<header class="abs header">
  <div class="abs logo"><span class="dot"></span><span class="brand-name">Brightvale Outfitters Co.</span></div>
  <nav class="abs nav">
    <span class="active">HOME</span><span>ABOUT US</span><span>PRODUCTS ⌄</span><span>BLOG</span><span>CONTACT US</span>
  </nav>
  <div class="abs search">
    <svg width="13" height="13" viewBox="0 0 24 24"><circle cx="10" cy="10" r="7" fill="none" stroke="#ef6420" stroke-width="3"/><path d="M15 15l6 6" stroke="#ef6420" stroke-width="3"/></svg>
    Search
  </div>
</header>

<section class="abs hero">
  <div class="hero-photo" role="img" aria-label="Young woman in a grey hoodie leaning against a dark wall"></div>
  <h1 class="abs hero-title">DREAMS DON'T WORK<br>UNLESS YOU DO</h1>
  <a class="abs btn">SHOP NOW</a>
  <svg class="abs hero-wave" width="1200" height="670" viewBox="0 0 1200 670">
    <path d="M0 455 Q600 840 1200 455 L1200 670 L0 670Z" fill="#fff"/>
    <path d="M0 455 Q300 647 600 658" fill="none" stroke="#ef6420" stroke-width="9"/>
    <path d="M600 658 Q900 647 1200 455" fill="none" stroke="#1d5c94" stroke-width="9"/>
  </svg>
  <div class="abs dots"><span></span><span class="on"></span><span></span><span></span></div>
</section>

<section class="collections">
  <span class="abs mark dot" style="top:897px"></span>
  <h2 class="abs heading" style="top:963px">NEW COLLECTIONS</h2>
  <div class="abs collection c-hoodies" role="img" aria-label="Three young men wearing black hoodies"><span class="label">HOODIES</span></div>
  <div class="abs collection c-tees" role="img" aria-label="Woman holding a basketball outdoors"><span class="label">T-SHIRTS</span></div>
</section>

<section class="abs featured">
  <span class="abs mark dot" style="top:76px"></span>
  <h2 class="abs heading" style="top:142px">FEATURED PRODUCTS</h2>
  <div class="abs arrow" style="left:30px;top:407px"><svg width="10" height="10" viewBox="0 0 10 10"><path d="M7 1L3 5l4 4" fill="none" stroke="#222" stroke-width="1.6"/></svg></div>
  <div class="abs arrow" style="left:1134px;top:407px"><svg width="10" height="10" viewBox="0 0 10 10"><path d="M3 1l4 4-4 4" fill="none" stroke="#222" stroke-width="1.6"/></svg></div>

  <article class="abs product" style="left:112px">
    <div class="shot" role="img" aria-label="Black crew-neck t-shirt" style="background:linear-gradient(#2a2a2a,#0e0e0e)"></div>
    <h3>BRIGHTVALE PRESTIGIOUS TEE</h3>
    <p>This t-shirt is everything you've dreamed of and more.</p>
    <div class="price">$19.99 USD</div>
  </article>
  <article class="abs product is-active" style="left:452px">
    <div class="shot" role="img" aria-label="Navy long-sleeve tee" style="background:linear-gradient(#2c4678,#1a2c55)"></div>
    <a class="btn">SHOP NOW</a>
    <h3>BRIGHTVALE TO THE MOON TEE</h3>
    <p>This t-shirt is everything you've dreamed of and more.</p>
    <div class="price">$19.99 USD</div>
  </article>
  <article class="abs product" style="left:794px">
    <div class="shot" role="img" aria-label="Black pullover hoodie" style="background:linear-gradient(#262626,#0b0b0b)"></div>
    <h3>BRIGHTVALE PRESTIGIOUS TEE</h3>
    <p>This t-shirt is everything you've dreamed of and more.</p>
    <div class="price">$19.99 USD</div>
  </article>
</section>

<section class="abs mission" role="img" aria-label="Orange-toned photo of a smiling man against a brick wall">
  <span class="abs mark dot" style="top:67px"></span>
  <h2 class="abs heading" style="top:136px">OUR MISSION &amp; VISION</h2>
  <div class="abs mbox" style="left:112px;width:475px">
    <div class="icon" style="left:189px">
      <svg width="46" height="46" viewBox="0 0 46 46" fill="none" stroke="#1d5c94" stroke-width="2.5"><circle cx="23" cy="23" r="18"/><circle cx="23" cy="23" r="11"/><circle cx="23" cy="23" r="4"/><path d="M23 23L40 6M34 6h6v6"/></svg>
    </div>
    <h3>OUR MISSION</h3>
    <p>My mission is to inspire young kids of color to chase a dream and to motivate them to pursue a purpose and look fashionable while doing it.</p>
  </div>
  <div class="abs mbox" style="left:611px;width:477px">
    <div class="icon" style="left:190px">
      <svg width="46" height="46" viewBox="0 0 46 46" fill="none" stroke="#1d5c94" stroke-width="2.5"><path d="M6 40V28M16 40V20M26 40V24M36 40V14M4 40h38"/><path d="M8 22l10-9 8 5 12-12"/><circle cx="38" cy="6" r="2"/></svg>
    </div>
    <h3>OUR VISION</h3>
    <p>My vision is to create quality products representing my brand and sharing the brand image with customers around the world. My ultimate goal is to create a community around the brand that has a meaningful purpose.</p>
  </div>
</section>

<section class="story">
  <div class="abs story-photo" role="img" aria-label="Two young men in branded tees standing by a fountain"></div>
  <span class="abs mark dot" style="top:2966px"></span>
  <h2 class="abs" style="top:3027px">BRAND STORY</h2>
  <p class="abs" style="top:3085px">BRIGHTVALE started a concept in my childhood of making it out of poverty and creating opportunities through work ethic and vision which came from the space theme. I would plan with patience how I would take the next steps toward my future.</p>
  <a class="abs btn">READ MORE</a>
</section>

<section class="abs reviews">
  <span class="abs mark dot" style="top:66px"></span>
  <h2 class="abs heading" style="top:140px">OUR CUSTOMER REVIEWS</h2>
  <div class="abs arrow" style="left:37px;top:359px"><svg width="10" height="10" viewBox="0 0 10 10"><path d="M7 1L3 5l4 4" fill="none" stroke="#222" stroke-width="1.6"/></svg></div>
  <div class="abs arrow" style="left:1129px;top:359px"><svg width="10" height="10" viewBox="0 0 10 10"><path d="M3 1l4 4-4 4" fill="none" stroke="#222" stroke-width="1.6"/></svg></div>

  <article class="abs review" style="left:112px">
    <div class="avatar" role="img" aria-label="Customer portrait"></div>
    <span class="quote" style="left:18px;top:112px">“</span>
    <p>Lorem ipsum dolor sit amet, consectetur adipiscing elit, sed do eiusmod tempor incididunt ut labore et dolore magna aliqua.</p>
    <span class="quote" style="right:18px;top:178px">”</span>
    <div class="who">- Olivia Kelly</div>
    <div class="stars">★★★★★</div>
  </article>
  <article class="abs review" style="left:446px">
    <div class="avatar" role="img" aria-label="Customer portrait"></div>
    <span class="quote" style="left:18px;top:112px">“</span>
    <p>Lorem ipsum dolor sit amet, consectetur adipiscing elit, sed do eiusmod tempor incididunt ut labore et dolore magna aliqua.</p>
    <span class="quote" style="right:18px;top:178px">”</span>
    <div class="who">- John Smith</div>
    <div class="stars">★★★★★</div>
  </article>
  <article class="abs review" style="left:780px">
    <div class="avatar" role="img" aria-label="Customer portrait"></div>
    <span class="quote" style="left:18px;top:112px">“</span>
    <p>Lorem ipsum dolor sit amet, consectetur adipiscing elit, sed do eiusmod tempor incididunt ut labore et dolore magna aliqua.</p>
    <span class="quote" style="right:18px;top:178px">”</span>
    <div class="who">- Marcus Delane</div>
    <div class="stars">★★★★★</div>
  </article>
</section>

<svg class="abs footer-arch" width="1200" height="475" viewBox="0 0 1200 475">
  <path d="M0 220 Q600 -130 1200 220 L1200 475 L0 475Z" fill="#1e1e1e"/>
  <path d="M0 210 Q300 37 600 45" fill="none" stroke="#ef6420" stroke-width="10"/>
  <path d="M600 45 Q900 37 1200 210" fill="none" stroke="#1d5c94" stroke-width="10"/>
</svg>

<footer class="abs footer">
  <div class="abs logo"><span class="dot"></span><span class="brand-name">Brightvale Outfitters Co.</span></div>

  <h4 class="abs" style="left:112px;top:105px">QUICK LINKS</h4>
  <div class="abs links" style="left:112px;top:153px">Home<br>About Us<br>Products<br>Contact Us</div>
  <div class="abs links" style="left:334px;top:153px">Blog<br>Privacy Policy<br>Terms Of Use</div>
  <div class="abs socials"><span></span><span></span><span></span><span></span><span></span></div>

  <h4 class="abs" style="left:596px;top:105px">JOIN OUR NEWSLETTER</h4>
  <div class="abs newsletter-input">Enter Your Email Here</div>
  <a class="abs btn">SUBSCRIBE</a>

  <div class="abs contact" style="left:596px;top:230px">
    <svg width="14" height="14" viewBox="0 0 24 24"><path fill="#ef6420" d="M6.6 10.8a15 15 0 0 0 6.6 6.6l2.2-2.2c.3-.3.7-.4 1-.2 1.1.4 2.3.6 3.6.6.6 0 1 .4 1 1V20c0 .6-.4 1-1 1A17 17 0 0 1 3 4c0-.6.4-1 1-1h3.5c.6 0 1 .4 1 1 0 1.3.2 2.5.6 3.6.1.3 0 .7-.2 1z"/></svg>
    <span>+1555-014-2290</span><span style="margin:0 20px">|</span>
    <svg width="16" height="12" viewBox="0 0 16 12"><rect width="16" height="12" rx="1" fill="#ef6420"/><path d="M1 1l7 6 7-6" fill="none" stroke="#1e1e1e" stroke-width="1.4"/></svg>
    <span>hello@brightvaleoutfitters.com</span>
  </div>

  <div class="abs rule"></div>
  <div class="abs copy">© 2023 BRIGHTVALE.Outfitters | All Rights Reserved</div>
  <div class="abs cards"><span></span><span></span><span></span><span></span><span></span></div>
</footer>

</body>
</html>
```